VarnoBud CBD Tincture packaging design

We are seeking a designer to create the label that will be printed on cardboard box packaging, which will carry our CBD tincture. We envision the box being white to resemble a clean look that stands out on shelves. Our logo (attached) uses shades of yellows and greens in the form of a fluid drop resembling half plant and half plant extract. The packaging will show that we only use clean (TRELK certified) hemp extract thats been extracted using the cleanest method of extraction; supercritical CO2. Our tincture uses a fractionated coconut oil to improve absorption for the consumer, increasing onset time and providing essential omega fatty acids. We take pride in our use of a clean product with a clean extraction. The tincture bottle itself holds 30ml of liquid and is a clear glass bottle. The cap for the tincture bottle is white and has a graduated glass stem that shows the measurements for how much liquid it holds (picture attached). We have not yet done the label that will stick on the tincture, but i image it will be a frosted white label with the VarnoBud logo and a few words describing the product. This project is for the cardboard box that will hold each individual tincture bottle.

BOX DIMENSIONS: 1.31" x 1.31" x 4.13" (LxWxH)

We will be releasing a new product (cbd capsules) in April, and we will reach out to the designer of this product as first option to create the design for the capsule packaging.

Target Market(s)

convenience stores, medical marijuana dispensaries, health stores

Font styles to use
Serif

Colors
ffffff
fbed22
ffc214
ffcf3e
acd136
9bcb3c

Requirements
Must have
• -VarnoBud company logo
-Made with full spectrum supercritical CO2 Hemp Extract
-Made from TRELK certified clean hemp
-Declaration of ingredients (fractionated coconut oil, CBD hemp extract)
-1200mg CBD Tincture
-Nt. Wt. 1FL OZ (30ml)
-These statements have not been evaluated by the Bureau of Remedy Oversight. BRO has not evaluated this product for safety or efficacy. This product is not intended to diagnose, treat, cure or prevent any disease.
-DO NOT REFRIGERATE. Keep at room temperature to preserve freshness. Store away from humidity, heat, and light. Warning: If pregnant, nursing or taking prescription drugs, consult your physician prior to use. Keep out of reach of children.
-Manufactured by VarnoBud CBD Co. 58 Corrow Bend Ln. Fennmoor, WA 04091
-Batch ID:___________
-Expiration Date:____________
-Good Manufacturing Practice (GMP) Logo
-TRELK logo
Nice to have
• -Contains omega 3, 6 and essential fatty acids
-Graduated dropper for precise dosing
-40mg of CBD per dropper!
-Made in the USA
-No Pesticides
-No Solvents
-No Heavy Metals
-CO2 Extraction
-3rd Party Lab Tested

```html
<!DOCTYPE html>
<html lang="en">
<head>
<meta charset="utf-8">
<title>VarnoBud CBD Tincture – Box Labels</title>
<link rel="stylesheet" href="https://fonts.googleapis.com/css2?family=Merriweather:wght@400;700&display=swap">
<style>
  :root {
    --page: #f8f8f8;
    --frame-gold: #c8861a;
    --frame-green: #2a9a2a;
    --ink: #222222;
    --panel-light: #ffffff;
    --panel-shade: #d9d9d9;
    --mark-gold: #d49a1c;
    --badge-green: #2f9a3a;
  }
  html, body {
    margin: 0;
    padding: 0;
    width: 1200px;
    height: 1200px;
    overflow: hidden;
    background: var(--page);
    font-family: "Merriweather", Georgia, serif;
    color: var(--ink);
  }
  .sheet {
    width: 1200px;
    height: 1200px;
    display: flex;
    justify-content: center;
    align-items: center;
    gap: 40px;
  }
  .label {
    position: relative;
    box-sizing: border-box;
    width: 500px;
    height: 750px;
    border: 3px solid var(--frame-gold);
    padding: 8px;
    background: radial-gradient(ellipse at 50% 50%, var(--panel-light) 0%, #efefef 55%, var(--panel-shade) 100%);
  }
  .label-inner {
    box-sizing: border-box;
    height: 100%;
    border: 2px solid var(--frame-green);
    display: flex;
    flex-direction: column;
    align-items: center;
    text-align: center;
  }

  /* Front */
  .claims {
    width: 100%;
    display: flex;
    justify-content: space-between;
    padding: 26px 34px 0;
    box-sizing: border-box;
    font-size: 12px;
    font-weight: 700;
  }
  .brand {
    margin-top: 70px;
    display: flex;
    align-items: center;
    gap: 16px;
  }
  .brand-dot {
    width: 46px;
    height: 46px;
    border-radius: 50%;
    background: var(--mark-gold);
  }
  .brand-name {
    font-size: 60px;
    font-weight: 700;
    color: var(--ink);
    letter-spacing: -1px;
  }
  .features {
    list-style: none;
    margin: 70px 0 0;
    padding: 0;
    font-size: 15px;
    font-weight: 700;
  }
  .features li { margin-bottom: 22px; }
  .maker {
    margin-top: auto;
    margin-bottom: 30px;
    font-size: 12.5px;
    font-weight: 700;
    line-height: 1.55;
  }

  /* Back */
  .info-box {
    margin-top: 40px;
    width: 446px;
    height: 300px;
    background: var(--panel-light);
    display: flex;
    flex-direction: column;
    align-items: center;
  }
  .section-title {
    margin: 40px 0 0;
    font-size: 14px;
    font-weight: 700;
  }
  .title-rule {
    width: 92px;
    height: 2px;
    background: var(--frame-green);
    margin: 14px 0 26px;
    border: 0;
  }
  .ingredients {
    font-size: 11.5px;
    font-weight: 700;
    line-height: 1.4;
    margin: 0;
  }
  .record {
    margin-top: 54px;
    align-self: flex-start;
    margin-left: 124px;
    font-size: 10.5px;
    font-weight: 700;
    text-align: left;
  }
  .record div { margin-bottom: 14px; }
  .record span { display: inline-block; width: 92px; }
  .attention-title {
    margin: 70px 0 18px;
    font-size: 11.5px;
    font-weight: 700;
  }
  .notice {
    margin: 0 0 14px;
    padding: 0 20px;
    font-size: 8.6px;
    font-weight: 700;
    line-height: 1.45;
  }
  .badges {
    margin-top: 44px;
    display: flex;
    gap: 22px;
  }
  .badge {
    width: 62px;
    height: 62px;
    border-radius: 50%;
    border: 3px solid var(--badge-green);
    box-sizing: border-box;
    background: radial-gradient(circle, #7cc47c 0%, #ffffff 70%);
  }
</style>
</head>
<body>
  <main class="sheet">
    <section class="label label-front" aria-label="Front panel">
      <div class="label-inner">
        <div class="claims">
          <span>No Pesticides</span>
          <span>No Solvents</span>
          <span>No Heavy Metals</span>
        </div>
        <div class="brand">
          <span class="brand-dot"></span>
          <span class="brand-name">VarnoBud</span>
        </div>
        <ul class="features">
          <li>Contains Omega 3, 6 and Essential Fatty Acids</li>
          <li>Graduated Dropper for Precise Dosing</li>
          <li>40mg of CBD per dropper</li>
          <li>Made in the USA</li>
        </ul>
        <p class="maker">Manufactured by<br>VarnoBud CBD Co. 58 Corrow Bend Ln. Fennmoor, WA 04091</p>
      </div>
    </section>

    <section class="label label-back" aria-label="Back panel">
      <div class="label-inner">
        <div class="info-box">
          <h2 class="section-title">INGERDIANTS</h2>
          <hr class="title-rule">
          <p class="ingredients">
            Full spectrum supercritical CO2 Hemp Extract<br>
            TRELK certified clean hemp<br>
            Declaration of ingredients (fractionated coconut oil, CBD hemp extract)<br>
            1200mg CBD Tincture<br>
            Nt. Wt. 1FL OZ (30ml)
          </p>
          <div class="record">
            <div><span>Batch ID</span>:</div>
            <div><span>Expiration Date</span>:</div>
          </div>
        </div>
        <h2 class="attention-title">ATTENTION</h2>
        <p class="notice">
          These Statements Have Not Been Evaluated By The Bureau Of Remedy Oversight.<br>
          BRO Has Not Evaluated This Product For Safety Or Efficacy. This Product Is Not Intended To Diagnose,<br>
          Treat, Cure Or Prevent Any Disease.<br>
          Do Not Refrigerate. Keep At Room Temperature To Preserve Freshness.<br>
          Store Away From Humidity, Heat, And Light.
        </p>
        <p class="notice">
          Warning: If Pregnant, Nursing Or Taking Prescription Drugs,<br>
          Consult Your Physician Prior To Use. Keep Out Of Reach Of Children.
        </p>
        <div class="badges">
          <span class="badge" role="img" aria-label="GMP certification badge"></span>
          <span class="badge" role="img" aria-label="TRELK certification badge"></span>
        </div>
      </div>
    </section>
  </main>
</body>
</html>
```